Business Card for Start Up Real Estate Company

We need a business card designed for a new real estate company called Lumivane. We plan on improving the experience of real estate transactions for both consumers and agents by using current and evolving technology. We would like to see designs that use our existing logo (attached). Please use a primarily white or light colored background. The final design should communicate technology, sophistication and customer service. Thank you...

Industry/Entity Type

Real Estate

Requirements
Must have
• Primarily white or light colored background
Nice to have
• Isolated A from our logo used as part of the design
Should not have
• Pictures, especially of houses

```html
<!DOCTYPE html>
<html lang="en">
<head>
<meta charset="UTF-8">
<title>Lumivane Business Card</title>
<link rel="stylesheet" href="https://fonts.googleapis.com/css2?family=Roboto:wght@300;400;700&display=swap">
<style>
  :root {
    --brand-blue: #005596;
    --brand-red: #e8213a;
    --text-grey: #767676;
    --card-white: #ffffff;
  }
  * { margin: 0; padding: 0; box-sizing: border-box; }
  html, body {
    width: 1200px;
    height: 686px;
    overflow: hidden;
    background: var(--card-white);
  }
  .card {
    position: relative;
    width: 1200px;
    height: 686px;
    background: var(--card-white);
    font-family: "Roboto", Arial, sans-serif;
    overflow: hidden;
  }
  .accent-band {
    position: absolute;
    height: 44px;
  }
  .accent-band-blue {
    left: 0;
    top: 420px;
    width: 640px;
    background: var(--brand-blue);
  }
  .accent-band-red {
    left: 680px;
    top: 310px;
    width: 520px;
    background: var(--brand-red);
  }
  .brand-block {
    position: absolute;
    left: 50px;
    top: 58px;
    width: 630px;
    text-align: center;
  }
  .brand-name {
    display: block;
    font-size: 100px;
    font-weight: 400;
    letter-spacing: 2px;
    line-height: 1;
    color: var(--brand-blue);
  }
  .office-address {
    margin-top: 20px;
    font-size: 34px;
    font-weight: 300;
    line-height: 43px;
    color: var(--text-grey);
    font-style: normal;
  }
  .person {
    position: absolute;
    right: 63px;
    top: 78px;
    text-align: right;
  }
  .person-name {
    font-size: 44px;
    font-weight: 700;
    line-height: 1.1;
    color: var(--brand-blue);
  }
  .person-title {
    margin-top: 2px;
    font-size: 34px;
    font-weight: 300;
    color: var(--text-grey);
  }
  .contact-line {
    position: absolute;
    display: flex;
    align-items: center;
    font-size: 42px;
    font-weight: 300;
    color: var(--text-grey);
    white-space: nowrap;
  }
  .contact-phone { right: 62px; top: 492px; gap: 18px; }
  .contact-email { right: 52px; top: 576px; gap: 8px; }
  .contact-web   { left: 80px; top: 576px; gap: 16px; }
  .icon { display: block; }
</style>
</head>
<body>
<main class="card">
  <div class="accent-band accent-band-blue" aria-hidden="true"></div>
  <div class="accent-band accent-band-red" aria-hidden="true"></div>

  <header class="brand-block">
    <span class="brand-name">LUMIVANE</span>
    <address class="office-address">742 Harlow Park Rd. 5th Floor<br>Fairmont, CA 94021</address>
  </header>

  <section class="person">
    <h1 class="person-name">Daniel Reyes</h1>
    <p class="person-title">CEO/Agent</p>
  </section>

  <p class="contact-line contact-phone">
    <span class="contact-text">800-555-0148</span>
    <svg class="icon icon-phone" width="40" height="70" viewBox="0 0 40 70" aria-hidden="true">
      <rect x="3" y="3" width="34" height="64" rx="5" fill="none" stroke="var(--brand-red)" stroke-width="4"/>
      <line x1="3" y1="13" x2="37" y2="13" stroke="var(--brand-red)" stroke-width="3"/>
      <line x1="3" y1="55" x2="37" y2="55" stroke="var(--brand-red)" stroke-width="3"/>
      <circle cx="20" cy="61" r="2.5" fill="var(--brand-red)"/>
    </svg>
  </p>

  <p class="contact-line contact-email">
    <span class="contact-text">info@lumivane.com</span>
    <svg class="icon icon-mail" width="64" height="46" viewBox="0 0 64 46" aria-hidden="true">
      <g fill="none" stroke="var(--brand-red)" stroke-width="4" stroke-linejoin="round">
        <polygon points="4,10 58,3 60,40 6,44"/>
        <polyline points="4,10 33,28 58,3"/>
        <line x1="6" y1="44" x2="27" y2="24"/>
        <line x1="60" y1="40" x2="40" y2="21"/>
      </g>
    </svg>
  </p>

  <p class="contact-line contact-web">
    <svg class="icon icon-globe" width="40" height="40" viewBox="0 0 40 40" aria-hidden="true">
      <g fill="none" stroke="var(--brand-red)" stroke-width="2.5">
        <circle cx="20" cy="20" r="17"/>
        <ellipse cx="20" cy="20" rx="8" ry="17"/>
        <line x1="20" y1="3" x2="20" y2="37"/>
        <line x1="3" y1="20" x2="37" y2="20"/>
        <path d="M6,11 H34 M6,29 H34"/>
      </g>
    </svg>
    <span class="contact-text">lumivane.com</span>
  </p>
</main>
</body>
</html>
```